Reputable business cards for Diplom Kauffrau, Privat und Geschäftslich

The business cards should be reputable, valuable and elegant in order to be able to use them for business. The design should also include a sophistication that is conspicuous. This could be a picture, an ornament, a sublime print or a kind of logo of the initials of my name "MK". The font should be clear and legible.
Target Market(s)
Business contacts, friends and acquaintances
Contact Information for Business Card
Diplom-Kauffrau Marietta Kuhnle
Lindenhofweg 37 50391 Haldernau
Mobil +49 170 418 29 57
e-mail marietta.kuhnle@postfeld.de
Font styles to use
Colors
Designer to choose colors to be used in the design.
Requirements
Must have
- Clear and easy to read font My name in larger font than the other information Visual conspicuity / specificity
Nice to have
- Different colors
Should not have
- Ornate font, playful

```html
<!DOCTYPE html>
<html lang="de">
<head>
<meta charset="utf-8">
<title>Visitenkarte Marietta Kuhnle</title>
<link rel="stylesheet" href="https://fonts.googleapis.com/css2?family=Questrial&family=Roboto:wght@400&display=swap">
<style>
  :root {
    --page-bg: #ffffff;
    --card-light: #f4f4f5;
    --card-light-shade: #dcdcde;
    --card-dark: #2b2d2e;
    --card-dark-deep: #1e2021;
    --accent-blue: #1ab8e0;
    --ink-dark: #1f1f1f;
    --ink-light: #ffffff;
    --ink-muted: #3a3a3a;
  }
  * { margin: 0; padding: 0; box-sizing: border-box; }
  html, body {
    width: 1200px;
    height: 900px;
    overflow: hidden;
    background: var(--page-bg);
  }
  .canvas {
    position: relative;
    width: 1200px;
    height: 900px;
  }
  .business-card {
    position: absolute;
    left: 160px;
    top: 165px;
    width: 880px;
    height: 570px;
    border-radius: 38px;
    overflow: hidden;
    box-shadow: 0 10px 30px rgba(0,0,0,0.18);
    display: flex;
    flex-direction: column;
  }
  .identity-panel {
    position: relative;
    height: 330px;
    flex: none;
  }
  .faceted-backdrop {
    position: absolute;
    inset: 0;
    background:
      linear-gradient(135deg, var(--card-light) 0%, #ffffff 35%, var(--card-light-shade) 70%, var(--card-light) 100%);
  }
  .identity-content {
    position: relative;
    height: 100%;
    display: flex;
    flex-direction: column;
    align-items: center;
    padding-top: 62px;
    font-family: "Questrial", sans-serif;
    font-weight: 400;
    color: var(--ink-dark);
  }
  .monogram {
    display: flex;
    align-items: center;
    gap: 14px;
    height: 120px;
  }
  .monogram-dot {
    width: 18px;
    height: 18px;
    border-radius: 50%;
    background: var(--ink-dark);
  }
  .monogram-letters {
    font-size: 92px;
    line-height: 1;
    letter-spacing: 2px;
  }
  .holder-name {
    margin-top: 28px;
    font-size: 44px;
    font-weight: 400;
    line-height: 1;
    letter-spacing: 0.5px;
  }
  .holder-title {
    margin-top: 14px;
    font-size: 15px;
    letter-spacing: 14px;
    margin-right: -14px;
    color: var(--ink-muted);
  }
  .accent-rule {
    height: 9px;
    flex: none;
    background: var(--accent-blue);
  }
  .contact-panel {
    position: relative;
    flex: 1;
  }
  .perforated-backdrop {
    position: absolute;
    inset: 0;
    background: linear-gradient(180deg, var(--card-dark) 0%, var(--card-dark-deep) 100%);
  }
  .contact-list {
    position: relative;
    list-style: none;
    text-align: center;
    font-family: "Roboto", sans-serif;
    font-weight: 400;
    color: var(--ink-light);
    padding-top: 42px;
  }
  .contact-phone {
    font-size: 29px;
    letter-spacing: 0.5px;
  }
  .contact-email,
  .contact-address {
    font-size: 22px;
    margin-top: 16px;
  }
</style>
</head>
<body>
<main class="canvas">
  <article class="business-card">
    <section class="identity-panel">
      <div class="faceted-backdrop" role="img" aria-label="Hellgrauer facettierter Polygon-Hintergrund"></div>
      <div class="identity-content">
        <div class="monogram">
          <span class="monogram-dot"></span>
          <span class="monogram-letters">MK</span>
        </div>
        <h1 class="holder-name">Kauffrau Marietta Kuhnle</h1>
        <p class="holder-title">DIPLOM</p>
      </div>
    </section>
    <div class="accent-rule"></div>
    <section class="contact-panel">
      <div class="perforated-backdrop" role="img" aria-label="Dunkles gelochtes Punktmuster"></div>
      <ul class="contact-list">
        <li class="contact-phone">+49 170 418 29 57</li>
        <li class="contact-email">marietta.kuhnle@postfeld.de</li>
        <li class="contact-address">Lindenhofweg 37 50391 Haldernau</li>
      </ul>
    </section>
  </article>
</main>
</body>
</html>
```